Redesign Of Flower Delivery Subscription Service Website

I need a revamped website of www.petal-rush.com

Please revamp current design using same content....

Target Market(s)

people who buy flowers. Brides, wedding planners, wedding photographer, married man, boyfriend, etc.

Industry/Entity Type

Florist

Number of Pages Required

5+ page

Colors

Designer to choose colors to be used in the design.

Requirements
Must have
• I need a revamped website of www.petal-rush.com
• Please revamp current design using same content....
Nice to have
Should not have

```html
<!DOCTYPE html>
<html lang="en">
<head>
<meta charset="utf-8">
<title>PetalRush – Monthly Flower Delivery</title>
<link href="https://fonts.googleapis.com/css2?family=Roboto:wght@300;400;500;700&family=Roboto+Condensed:wght@400;700&display=swap" rel="stylesheet">
<style>
:root{
  --black:#111;
  --panel:rgba(30,30,30,.88);
  --green:#7cbb3a;
  --green-dark:#3f7e10;
  --green-light:#a6d36a;
  --orange:#f7a81b;
  --text:#444;
  --footer:#3b3129;
  --footer-bar:#1d1814;
  --white:#fff;
}
*{margin:0;padding:0;box-sizing:border-box}
html,body{width:1200px;height:1200px;overflow:hidden;background:#fff;font-family:"Roboto",sans-serif;color:var(--text)}
.page{position:absolute;left:305.6px;top:0;width:735px;height:1500px;transform:scale(.8);transform-origin:0 0;background:#fff}
.abs{position:absolute}
.header{left:0;top:0;width:735px;height:38px;background:var(--black)}
.brand{left:102px;top:6px;font:500 19px "Roboto",sans-serif;color:var(--green);letter-spacing:.5px}
.brand-dot{display:inline-block;width:9px;height:9px;border-radius:50%;background:var(--green);margin-right:5px;vertical-align:middle}
.topcontact{right:100px;top:6px;font-size:9px;color:var(--green);display:flex;gap:10px;align-items:center}
.topcontact .mail{font-size:6px;color:#ccc}
.social{display:flex;gap:4px}
.social span{width:10px;height:10px;border-radius:50%;background:#666;display:block}
.nav{left:229px;top:25px;display:flex;gap:10px;font-size:7px;color:#ddd}
.nav .active{color:var(--green);text-decoration:underline}
.hero{left:0;top:38px;width:735px;height:256px;background:linear-gradient(90deg,#c7764a 0%,#e0ae8c 30%,#d8d2c2 55%,#e9e6dc 80%,#f3f3ef 100%)}
.arrow{top:140px}
.box{top:182px;height:112px;background:var(--panel);padding:20px 10px;color:var(--white)}
.box h2{font:700 15px "Roboto Condensed",sans-serif;display:flex;align-items:center;gap:4px}
.box h2::after{content:"";flex:1;height:1px;background:#888}
.box p{font-size:8px;margin-top:7px;line-height:1.3}
.price{font:500 12px "Roboto",sans-serif;color:var(--green-light);margin-top:3px}
.pill{display:inline-block;font:700 7.5px "Roboto",sans-serif;padding:3px 7px;border-radius:9px;margin-top:6px;margin-right:3px;border:1px solid #fff3}
.pill.orange{background:var(--orange);color:#5a3300}
.pill.green{background:var(--green);color:#1f3e06}
.field{height:20px;border-radius:10px;background:#222;border:1px solid #555;font-size:6px;color:#999;padding:6px 20px;margin-top:6px}
.btn{display:block;margin:8px auto 0;width:54px;height:15px;border-radius:8px;background:var(--orange);color:#5a3300;font:700 8px "Roboto",sans-serif;text-align:center;line-height:15px}
.crow{display:flex;gap:6px;align-items:flex-start;font-size:6.5px;margin-top:6px}
.crow.big{font-size:9px;color:var(--green-light)}
.photo{display:block}
.copy{font-size:6.5px;line-height:1.5;color:#555}
.copy h3{font:400 11px "Roboto",sans-serif;color:var(--green-dark);margin-bottom:5px}
.copy b{color:var(--green-dark);font-weight:500}
.intro{left:0;width:735px;text-align:center}
.intro.sub{top:884px;font:400 11px "Roboto",sans-serif;color:#555}
.intro.title{top:897px;font:500 22px "Roboto Condensed",sans-serif;color:var(--green-dark)}
.rule{height:1px;background:var(--green-light)}
.lead{left:104px;top:966px;width:528px;text-align:center;font-size:6.3px;line-height:1.7;color:#555}
.card{top:1036px;width:160px;height:206px;background:var(--green);box-shadow:0 4px 4px -2px #0003}
.card .side{position:absolute;left:0;top:0;width:34px;height:206px;background:var(--green-light)}
.card .side div{position:absolute;left:17px;top:103px;width:200px;transform:translate(-50%,-50%) rotate(-90deg);text-align:center;color:#3a5c12}
.card .side small{display:block;font-size:6px}
.card .side strong{display:block;font:700 10px "Roboto Condensed",sans-serif}
.card p{position:absolute;left:36px;top:14px;width:118px;font-size:6.2px;line-height:1.5;color:#fff}
.footer{left:0;top:1270px;width:735px;height:208px;background:radial-gradient(circle at 8% 45%,#5b4a2b,transparent 25%),radial-gradient(circle at 85% 55%,#574627,transparent 25%),var(--footer)}
.fcol h4{font:300 14px "Roboto",sans-serif;color:#ddd;margin-bottom:10px}
.fcol li{list-style:none;font-size:6.8px;color:#aaa;line-height:16px}
.ffield{width:168px;height:18px;border:1px solid #6a5d50;border-radius:3px;background:#2e261f;font-size:5.5px;color:#999;padding:5px 0 0 19px;margin-bottom:6px}
.ffield.area{height:46px}
.fbtn{width:110px;height:16px;border-radius:8px;background:var(--orange);color:#5a3300;font:700 8px "Roboto",sans-serif;text-align:center;line-height:16px;margin:4px 0 0 29px}
.fbar{left:0;top:1478px;width:735px;height:22px;background:var(--footer-bar);font-size:6px;color:#888;text-align:center;line-height:22px}
</style>
</head>
<body>
<div class="page">
  <header class="abs header"></header>
  <div class="abs brand"><span class="brand-dot"></span>PetalRush</div>
  <div class="abs topcontact">
    <span>&#9742; 555-214-0387</span>
    <span class="mail">&#9993; hello@petalrush.com</span>
    <span class="social"><span></span><span></span><span></span></span>
  </div>
  <nav class="abs nav">
    <span class="active">Home</span><span>How it Works</span><span>Delivery Areas</span><span>Franchise</span><span>My Account</span><span>Blog</span><span>Free Flowers Monthly</span><span>Corporate Arrangements</span><span>Help</span>
  </nav>

  <div class="abs hero" role="img" aria-label="Hero photo of a woman holding soft white blossoms"></div>
  <svg class="abs arrow" style="left:14px" width="30" height="60"><polyline points="28,2 2,30 28,58" fill="none" stroke="#fff" stroke-width="1"/></svg>
  <svg class="abs arrow" style="left:690px" width="30" height="60"><polyline points="2,2 28,30 2,58" fill="none" stroke="#fff" stroke-width="1"/></svg>

  <section class="abs box" style="left:99px;width:180px">
    <h2>ALWAYS FRESH</h2>
    <p>Beautiful Flower Arrangements Delivered Monthly Now only</p>
    <div class="price">$69.95/MTH ($100 value)</div>
    <span class="pill orange">FREE VASE</span><span class="pill green">FREE DELIVERY</span>
  </section>
  <section class="abs box" style="left:279px;width:178px;border-left:1px solid #444">
    <h2>A FREE UPGRADE</h2>
    <div class="field" style="margin-top:12px">Enter your mail ID</div>
    <span class="btn">SUBMIT</span>
  </section>
  <section class="abs box" style="left:457px;width:179px;border-left:1px solid #444">
    <h2>CONTACT INFO</h2>
    <div class="crow" style="margin-top:10px">
      <svg width="10" height="12"><path d="M5 1a4 4 0 0 1 4 4c0 3-4 6-4 6S1 8 1 5a4 4 0 0 1 4-4z" fill="none" stroke="#7cbb3a"/><circle cx="5" cy="5" r="1.4" fill="#7cbb3a"/></svg>
      <span>1840 Orchard Lane, Alder Bay<br>CA 90000</span>
    </div>
    <div class="crow big"><span style="color:#7cbb3a">&#9742;</span><span>555-214-0387</span></div>
    <div class="crow"><span style="color:#7cbb3a">&#9993;</span><span>hello@petalrush.com</span></div>
  </section>

  <div class="abs photo" style="left:279px;top:294px;width:178px;height:111px;background:linear-gradient(135deg,#f5e8ea,#eea3b3 55%,#d9637f)" role="img" aria-label="Pink rose bouquet"></div>
  <div class="abs photo" style="left:457px;top:294px;width:179px;height:111px;background:linear-gradient(180deg,#cfdff0,#c9d9a8 55%,#7a9a3a)" role="img" aria-label="Butterflies over a spring meadow"></div>
  <div class="abs photo" style="left:457px;top:405px;width:179px;height:112px;background:linear-gradient(135deg,#f3e6d3,#e8d1b6 50%,#8c4a5a)" role="img" aria-label="Cream roses arrangement"></div>

  <div class="abs copy" style="left:150px;top:430px;width:290px;text-align:right">
    <h3>Set it and forget it</h3>
    <p>PetalRush is a <b>"SET IT and FORGET IT"</b> subscription based<br>flower delivery service.</p>
    <p style="margin-top:6px">For an Amazing price PetalRush will hand deliver a gorgeous arrangement directly to anyone you want every month without you having to worry about it.</p>
  </div>

  <div class="abs photo" style="left:99px;top:517px;width:358px;height:199px;background:linear-gradient(135deg,#3d3a2a,#6b6a4a 40%,#e9a3b4 60%,#4a4530)" role="img" aria-label="Pink carnations resting on a wooden bench"></div>
  <div class="abs copy" style="left:467px;top:564px;width:172px">
    <h3>But never forget again</h3>
    <p>When setting up your account, you can choose exact delivery dates for the months that have special days such as your Anniversary, Birthday, Valentines Day and Mothers Day. You might forget but we won't, we have got ya covered!</p>
  </div>

  <div class="abs photo" style="left:99px;top:716px;width:179px;height:139px;background:linear-gradient(135deg,#c9d4d8,#8a4a8a 45%,#5a2a5a 75%,#c7b6cf)" role="img" aria-label="Purple and lilac flower bouquet"></div>
  <div class="abs copy" style="left:286px;top:750px;width:165px">
    <h3>Making Someone's day better</h3>
    <p>Be the hero in that special someone's life each and every month.</p>
    <p style="margin-top:9px">It feels good to make a difference in your loved ones day.</p>
  </div>

  <div class="abs intro sub">Monthly Subscription Based Flower Delivery Service in San Diego</div>
  <div class="abs intro title">– CA by Our Florist Shop</div>
  <div class="abs rule" style="left:226px;top:943px;width:124px"></div>
  <div class="abs rule" style="left:388px;top:943px;width:124px"></div>
  <div class="abs" style="left:356px;top:928px;width:26px;height:30px;border-radius:40% 40% 10% 10%;background:linear-gradient(180deg,#d8334a,#6aa83a)" role="img" aria-label="Small rose ornament"></div>

  <p class="abs lead">Every moment of life could be cherished perfectly......IF you choose wisely. To make your day more treasured, remember that flowers are the smartest choice when delivered through our monthly PetalRush subscription based delivery service. Our online subscription-based flower delivery service can help you pamper, cherish and make an everlasting impression on the minds of your loved ones with a doorstep delivery of exquisitely hand-designed floral arrangements. Our online subscription service features both standard and personalized services to help you choose from an assortment of classic and contemporary floral arrangements. It is your chance to setup a weekly, monthly, or quarterly subscription, so we can deliver the most exotic collections of hand-decorated flowers that you and your loved ones will cherish.</p>

  <article class="abs card" style="left:99px">
    <div class="side"><div><small>Exotic Flowers Garnished With Special Hues To</small><strong>Compliment Your Loved Ones</strong></div></div>
    <p>Let's not forget a single day in which you can make your loved ones feel special. Whether it's your anniversary or a birthday in your family, you must always go an extra mile to show "how much I care about you." Nothing can compare to your show of love, or compliment the joy of your loved ones, more than a perfectly blossomed bouquet of flowers. So if you are having difficulty in finding the perfect flower bouquet to share your overflowing love with that special person, don't worry.....PetalRush has got it all covered for you! We believe that our hand-picked and hand-designed flowers, created with a combination of lavish designs and feminine hues, will definitely grab the attention of your loved ones.</p>
  </article>
  <article class="abs card" style="left:287px">
    <div class="side"><div><small>Standard And Personalized Flower</small><strong>Arrangements For Special</strong></div></div>
    <p>PetalRush offers on time subscription based service that is risk free, trouble free and affordable at the same time. We offer the most trusted and delightful flower delivery service in Alder Bay, and are designed to deliver your desired floral arrangements within your requested days and times. Our local florists will happily take your orders online for your shopping convenience. You can count on us to deliver fresh flower baskets and bouquets for birthdays, weddings, mother's day, anniversaries and other special events within your locality, and even across the country. In case you're looking for something personalized, then our skilled florists can create custom arrangements for any special occasion.</p>
  </article>
  <article class="abs card" style="left:476px">
    <div class="side"><div><small>Get Yourself Subscribed And</small><strong>Claim Discounts On Big Orders!</strong></div></div>
    <p>Get love and adulation by gifting flowers to your loved ones on those special occasions. Whether it's formal, personal or your love for your family, just follow the subscription criteria and get your hands on the most valuable service for all kinds of events, occasions and parties. Set up your account and select the right delivery dates for the special months and leave the rest to us. We will deliver your flowers on the exact special dates to make your loved one's day wonderful. It is your chance to experience the simple, risk-free and trouble-free delivery of flowers right to the doorstep of your cherished loved</p>
  </article>

  <footer class="abs footer" role="img" aria-label="Dimmed sunflower background"></footer>
  <div class="abs fcol" style="left:98px;top:1292px">
    <h4>Quick Links:</h4>
    <ul><li>- Home</li><li>- How it Works</li><li>- Delivery Areas</li><li>- Franchise</li><li>- My Account</li><li>- Blog</li><li>- Free Flowers Monthly</li><li>- Corporate Arrangements</li><li>- Help</li></ul>
  </div>
  <div class="abs fcol" style="left:286px;top:1292px">
    <h4>More Services:</h4>
    <ul><li>- Corporate Arrangements</li><li>- Hotel Arrangements</li><li>- Events</li><li>- Weddings</li></ul>
  </div>
  <div class="abs fcol" style="left:468px;top:1292px">
    <h4>Get a Quote:</h4>
    <div class="ffield">Enter your Name</div>
    <div class="ffield">Enter Phone Number</div>
    <div class="ffield">Enter valid mail ID</div>
    <div class="ffield area">Comments</div>
    <div class="fbtn">SUBMIT</div>
  </div>
  <div class="abs fbar">Copyright © 2018 - Monthly Flowers Delivery - All rights reserved.</div>
</div>
</body>
</html>
```